Customer flyer

Hi there,

We need a flyer done for our father's business. It is called Tidal crest and the flyer will be distributed to realtors in British Columbia. He lends money to realtors when they have sold a home from the time subjects are removed from the transaction to when the sale closes. He is looking for a modern, classy look with the following information:

"Tidal Crest"

Realtor Pay Day upon Subject Removal

Did you know?

* Fees 100% tax deductable
* Same Day Service
* Confidential
* Low Rates

Your money from 738519 B.C. Ltd. and It can be directly deposited into your bank account or delivered to your office

For quote: call Gavin Merrow 250 555 0137

This is a small business so he doesn't have a logo and has never needed to do promotions before as it's run on word of mouth for the past 10 years. We are open to all ideas and suggestions - he is a finance guy so looking to you for the creative side :)

Thank you!

I don't like the phrase Realtor Pay Day upon subject removal. I think I prefer "Realtors! Celebrate Your Home sales upon subject removal" . Your thoughts?

Thank you

```html
<!DOCTYPE html>
<html lang="en">
<head>
<meta charset="utf-8">
<title>Tidal Crest – Realtor Flyer</title>
<link href="https://fonts.googleapis.com/css2?family=Cinzel:wght@500;600;700&family=Open+Sans:ital,wght@0,400;0,600;1,400&display=swap" rel="stylesheet">
<style>
  :root {
    --page-bg: #ebe7df;
    --paper: #ffffff;
    --green-deep: #1f5e0f;
    --green-mid: #3f8219;
    --green-bright: #5aa023;
    --green-pale: #d6e3cb;
    --ink: #2b2b2b;
    --suit-dark: #1c1c1e;
    --suit-mid: #3a3a3d;
    --white: #ffffff;
  }
  * { box-sizing: border-box; margin: 0; padding: 0; }
  html, body {
    width: 1200px; height: 900px; overflow: hidden;
    background: var(--page-bg);
  }
  .flyer {
    position: absolute; left: 312px; top: 44px;
    width: 576px; height: 810px;
    background: var(--paper);
    overflow: hidden;
    box-shadow: 4px 6px 14px rgba(0,0,0,.25);
    font-family: "Open Sans", Arial, sans-serif;
    color: var(--ink);
  }
  .hero-photo {
    position: absolute; left: 120px; top: 0; right: 0; bottom: 0;
    background:
      linear-gradient(100deg, var(--paper) 0%, #f4f4f2 28%, #b9b6ae 40%, var(--suit-mid) 52%, var(--suit-dark) 78%, #2d3a2a 100%);
  }
  .brand {
    position: absolute; left: 80px; top: 36px;
    font-family: "Cinzel", Georgia, serif;
    font-weight: 600;
    color: var(--green-mid);
    font-size: 62px; line-height: 62px;
    letter-spacing: 1px;
  }
  .brand span { display: block; }
  .brand span + span { padding-left: 60px; }
  .headline-band {
    position: absolute; left: 0; right: 0; top: 401px; height: 46px;
    background: linear-gradient(90deg, var(--green-deep), var(--green-mid) 60%, var(--green-deep));
    color: var(--white);
    font-family: "Cinzel", Georgia, serif;
    font-weight: 500;
    font-size: 20px; letter-spacing: 1px;
    display: flex; align-items: center; justify-content: center;
    z-index: 3;
  }
  .facts-shape { position: absolute; left: 0; top: 447px; z-index: 2; }
  .facts {
    position: absolute; left: 40px; top: 466px; width: 250px;
    text-align: center; z-index: 3;
  }
  .facts-title {
    font-family: "Cinzel", Georgia, serif;
    font-weight: 600; font-size: 18px; letter-spacing: .5px;
    color: #1e1e1e; margin-bottom: 12px;
  }
  .facts-list { list-style: none; font-size: 16px; line-height: 22px; color: #1e1e1e; }
  .facts-list .mark { color: var(--green-mid); font-weight: 600; margin-right: 5px; }
  .quote-badge { position: absolute; left: 244px; top: 560px; z-index: 3; }
  .quote-text {
    position: absolute; left: 244px; top: 560px; width: 298px; height: 192px;
    z-index: 4; color: var(--white); text-align: center;
    display: flex; flex-direction: column; align-items: center; justify-content: center;
  }
  .quote-lead { font-style: italic; font-size: 16px; letter-spacing: .5px; margin-bottom: 8px; opacity: .92; }
  .quote-name { font-family: "Cinzel", Georgia, serif; font-weight: 500; font-size: 31px; letter-spacing: 1px; line-height: 36px; }
  .quote-phone { font-size: 20px; letter-spacing: 1px; margin-top: 6px; }
  .fine-print {
    position: absolute; left: 30px; top: 722px; width: 250px;
    text-align: center; font-size: 12px; line-height: 15px; color: #333;
    z-index: 3;
  }
</style>
</head>
<body>
  <main class="flyer">
    <div class="hero-photo" role="img" aria-label="Photo of a businessman in a dark pinstripe suit and green tie holding up a house key"></div>

    <div class="brand"><span>Tidal</span><span>Crest</span></div>

    <div class="headline-band">REALTOR PAY DAY&nbsp; UPON SUBJECT REMOVAL</div>

    <svg class="facts-shape" width="360" height="180" viewBox="0 0 360 180" aria-hidden="true">
      <defs>
        <linearGradient id="factsFill" x1="0" y1="0" x2="0" y2="1">
          <stop offset="0" stop-color="#ecf2e5"/>
          <stop offset="1" stop-color="#cbdcbd"/>
        </linearGradient>
      </defs>
      <ellipse cx="160" cy="20" rx="190" ry="150" fill="url(#factsFill)"/>
    </svg>

    <section class="facts">
      <h2 class="facts-title">Did you know?</h2>
      <ul class="facts-list">
        <li><span class="mark">$</span>Fees 100% tax deductible</li>
        <li><span class="mark">$</span>Same Day Service</li>
        <li><span class="mark">$</span>Confidential</li>
        <li><span class="mark">$</span>Low Rates</li>
      </ul>
    </section>

    <svg class="quote-badge" width="298" height="192" viewBox="0 0 298 192" aria-hidden="true">
      <defs>
        <radialGradient id="badgeFill" cx="0.45" cy="0.4" r="0.7">
          <stop offset="0" stop-color="#2f7a18"/>
          <stop offset="1" stop-color="#1a5a0c"/>
        </radialGradient>
      </defs>
      <ellipse cx="149" cy="96" rx="147" ry="94" fill="url(#badgeFill)" stroke="#ffffff" stroke-width="2"/>
      <ellipse cx="149" cy="96" rx="134" ry="82" fill="none" stroke="#ffffff" stroke-width="1.5" opacity=".9"/>
    </svg>

    <div class="quote-text">
      <p class="quote-lead">For a quote call …</p>
      <p class="quote-name">Gavin Merrow</p>
      <p class="quote-phone">250 555 0137</p>
    </div>

    <p class="fine-print">Your money from 738519 B.C. Ltd. and It can be directly deposited into your bank account or delivered to your office</p>
  </main>
</body>
</html>
```